Etiketten-Design für Getränkedose
Zielgruppe
Ich werde Getränke in Dosen 250 ml herstellen lassen, welches ich im Markt vertreiben möchte.
Aufgabenstellung
Das Pfandlogo und die EAN müssen an die Etiketten rangebracht werden, deshalb ist es wichtig, dass wenn Sie keine Möglichkeit haben die EAN ranzubringen, dass Platz im Design frei gehalten wird.
Im Anhang 1 finden Sie die Abmessungen von den Etiketten die an die Dosen rangebracht werden sollen!
Das Design muss innerhalb von diesen Abmessungen erstellt werden.
Es handelt sich hier nur um eine Druckvorlage!
Für so eine Druckvorlage muss auf den Etiketten Platz frei gehalten werden.
Ich benötige von Ihnen 3D Dosendesigns, sowie in meiner Skizze.
Wichtig: Es sollen auschließlich die Farben Weiß und Grün genutzt werden.
Meine Marke heißt ' Silver Quince' und es ist wichtig, dass die Farbe grün mit der Limette von meinem Logo passt.
Anhang 2&3= Mein Logo
Anhang 4= Eine Skizze von mir.
Ganz oben am Dosenrand soll das Wort Lemon in Grün NICHT mit eingeführt werden.
Ganz unten soll bitte in Farbe Grau die Zahl: (2018) auf Römisch hinzugefügt werden und das Grau und die Schrift soll bitte mit meinem Logo passen:
MMXVIII
Wichtig: Es soll ein edles und modernes Design werden!
Ich freue mich auf Ihre kreativen Designs.
Als Vorgabe: Die Dose soll weiß sein und es sollen grüne Farben benutzt werden und es soll mit dem Logo farblich übereinstimmen.
Vielen Dank im Voraus

```html
<!DOCTYPE html>
<html lang="de">
<head>
<meta charset="utf-8">
<title>Silver Quince – Dosenetikett</title>
<link rel="stylesheet" href="https://fonts.googleapis.com/css2?family=Montserrat:wght@300&display=swap">
<style>
  :root {
    --label-white: #ffffff;
    --page-bg: #f4f4f4;
    --name-grey: #8a8a8a;
    --faint-grey: #ececec;
    --fainter-grey: #f1f1f1;
    --year-grey: #7c7c7c;
    --lime-green: #7dc242;
  }
  html, body {
    margin: 0;
    padding: 0;
    overflow: hidden;
    background: var(--page-bg);
  }
  .can-label {
    position: relative;
    width: 735px;
    height: 1200px;
    overflow: hidden;
    background: var(--label-white);
    font-family: "Montserrat", sans-serif;
    font-weight: 300;
  }
  .backdrop-word {
    position: absolute;
    margin: 0;
    font-size: 120px;
    font-weight: 300;
    line-height: 1;
    letter-spacing: 0.12em;
    white-space: nowrap;
    transform-origin: center;
  }
  .backdrop-word--right {
    color: var(--faint-grey);
    left: 660px;
    top: 520px;
    transform: translate(-50%, -50%) rotate(90deg);
  }
  .backdrop-word--left {
    color: var(--fainter-grey);
    left: 75px;
    top: 680px;
    transform: translate(-50%, -50%) rotate(-90deg);
  }
  .brand-name {
    position: absolute;
    left: 50%;
    top: 600px;
    transform: translate(-50%, -50%);
    display: flex;
    align-items: center;
    gap: 14px;
    margin: 0;
    color: var(--name-grey);
    font-size: 30px;
    font-weight: 300;
    letter-spacing: 0.1em;
    white-space: nowrap;
  }
  .brand-name__dot {
    width: 24px;
    height: 24px;
    border-radius: 50%;
    background: var(--lime-green);
    flex: none;
  }
  .year-dot {
    position: absolute;
    left: 367px;
    top: 1065px;
    width: 12px;
    height: 12px;
    border-radius: 50%;
    background: var(--year-grey);
    transform: translate(-50%, -50%);
  }
  .vintage-year {
    position: absolute;
    left: 0;
    right: 0;
    top: 1100px;
    margin: 0;
    text-align: center;
    color: var(--year-grey);
    font-size: 22px;
    letter-spacing: 0.2em;
  }
</style>
</head>
<body>
  <main class="can-label">
    <p class="backdrop-word backdrop-word--right" aria-hidden="true">SILVER</p>
    <p class="backdrop-word backdrop-word--left" aria-hidden="true">QUINCE</p>

    <h1 class="brand-name">
      <span class="brand-name__dot" aria-hidden="true"></span>
      SILVER QUINCE
    </h1>

    <span class="year-dot" aria-hidden="true"></span>
    <p class="vintage-year">MMXVII</p>
  </main>
</body>
</html>
```